Meridian Vessel, Inc. - Travel Worldwide
New Biz Cards for Modern Female Run Travel Agency - Travel
New Biz Cards for Modern Female Run Travel Agency
Simple
Loretta Pim, CTC
Owner
Boston, NY, Worldwide
loretta@meridianvessel-example.com
www.meridianvessel-example.com
We will need the same designed biz card for 2 main employees: Loretta Pim, CTC (Owner) loretta@meridianvessel-example.com Tamsin Ulwick, CTA (International Travel Consultant and Lead Planner) tamsin@meridianvessel-example.com
Honeymoons Destination Weddings Luxury Leisure Travel Your personal travel concierge.
MeridianVessel MeridianVessel
Hi plumquarto, thanks for all your submissions. we are reviewing and determining what we like and don't like. FYI what we like: 2 sided designs, clean lines, gray shading what we don't like: 1 sided designs, color fading, swirls/curves, duplicating designs on both sides, overuse of the logo THANK YOU
Hi Gondy, thanks for your submissions. a bit of text that we wanted to be included is missing, however. if you want to resubmit with that text, we have updated it to be: "Luxury Leisure Travel Honeymoons Destination Events Personal Travel Concierge"

```html
<!DOCTYPE html>
<html lang="en">
<head>
<meta charset="utf-8">
<title>Meridian Vessel – Business Card</title>
<link rel="stylesheet" href="https://fonts.googleapis.com/css2?family=Jura:wght@400;500&family=Oswald:wght@500;600&display=swap">
<style>
  :root {
    --backdrop: #2b2b2d;
    --card-white: #ffffff;
    --card-black: #0b0b0b;
    --ink-light: #f2f2f2;
    --ink-grey: #8a8a8a;
    --ink-dark: #6e6e6e;
  }
  * { margin: 0; padding: 0; box-sizing: border-box; }
  html, body {
    width: 1200px; height: 816px; overflow: hidden;
    background: var(--backdrop);
  }
  .card {
    position: absolute; left: 100px; top: 122px;
    width: 1000px; height: 572px;
    border-radius: 30px; overflow: hidden;
    background: var(--card-black);
  }
  .card__brand-side {
    position: absolute; left: 0; top: 0; width: 430px; height: 100%;
    background: var(--card-white);
  }
  .card__notch { position: absolute; left: 428px; top: 448px; }
  .brand {
    position: absolute; left: 0; top: 240px; width: 430px;
    text-align: center; font-family: "Jura", sans-serif; color: var(--ink-dark);
  }
  .brand__dot {
    display: block; width: 46px; height: 46px; margin: 0 auto 18px;
    border-radius: 50%; background: var(--ink-grey);
  }
  .brand__name {
    font-size: 27px; font-weight: 500; letter-spacing: 4px; text-transform: uppercase;
  }
  .brand__tagline {
    margin-top: 6px; font-size: 11px; letter-spacing: 4px; text-transform: uppercase;
    color: var(--ink-grey);
  }
  .contact {
    position: absolute; left: 462px; top: 58px; width: 510px;
    font-family: "Jura", sans-serif; color: var(--ink-light);
    font-size: 20px; font-weight: 500; letter-spacing: 1px; text-transform: uppercase;
    list-style: none;
  }
  .contact__item {
    display: flex; align-items: flex-start; gap: 12px; margin-bottom: 16px;
  }
  .contact__icon { flex: none; width: 20px; height: 20px; margin-top: 2px; }
  .contact__text { line-height: 1.3; white-space: nowrap; }
  .divider {
    position: absolute; left: 462px; top: 352px; width: 420px;
    border-top: 3px dotted var(--ink-light);
  }
  .person {
    position: absolute; right: 110px; top: 392px; text-align: right;
    font-family: "Oswald", sans-serif; color: var(--ink-light); text-transform: uppercase;
  }
  .person__name { font-size: 44px; font-weight: 600; letter-spacing: 2px; line-height: 1.1; white-space: nowrap; }
  .person__role { font-size: 27px; font-weight: 500; letter-spacing: 1px; }
</style>
</head>
<body>
  <div class="card">
    <div class="card__brand-side"></div>
    <svg class="card__notch" width="24" height="36" viewBox="0 0 24 36"><path d="M0 0 L24 18 L0 36 Z" fill="#ffffff"/></svg>

    <div class="brand">
      <span class="brand__dot"></span>
      <p class="brand__name">Meridian Vessel</p>
      <p class="brand__tagline">Personal Travel Concierge</p>
    </div>

    <ul class="contact">
      <li class="contact__item">
        <svg class="contact__icon" viewBox="0 0 20 20"><path d="M5 2 L8 2 L9 6 L7 8 C8 11 9 12 12 13 L14 11 L18 12 L18 15 C18 17 16 18 14 18 C8 17 3 12 2 6 C2 4 3 2 5 2 Z" fill="#f2f2f2"/></svg>
        <span class="contact__text">+1 (555) 014-2290</span>
      </li>
      <li class="contact__item">
        <svg class="contact__icon" viewBox="0 0 20 20"><rect x="2" y="4" width="16" height="12" fill="#f2f2f2"/><path d="M2 4 L10 11 L18 4" fill="none" stroke="#0b0b0b" stroke-width="1.6"/></svg>
        <span class="contact__text">loretta@meridianvessel-example.com</span>
      </li>
      <li class="contact__item">
        <svg class="contact__icon" viewBox="0 0 20 20"><circle cx="10" cy="10" r="8" fill="none" stroke="#f2f2f2" stroke-width="2"/><ellipse cx="10" cy="10" rx="3.5" ry="8" fill="none" stroke="#f2f2f2" stroke-width="1.5"/><line x1="2" y1="10" x2="18" y2="10" stroke="#f2f2f2" stroke-width="1.5"/></svg>
        <span class="contact__text">www.meridianvessel-example.com</span>
      </li>
      <li class="contact__item">
        <svg class="contact__icon" viewBox="0 0 20 20"><path d="M10 2 L19 10 L16 10 L16 18 L12 18 L12 13 L8 13 L8 18 L4 18 L4 10 L1 10 Z" fill="#f2f2f2"/></svg>
        <span class="contact__text">Boston, NY,<br>Worldwide</span>
      </li>
    </ul>

    <div class="divider"></div>

    <div class="person">
      <p class="person__name">Loretta Pim, CTC</p>
      <p class="person__role">Owner</p>
    </div>
  </div>
</body>
</html>
```